Webdesign für Installation, Wartung und Modernisierung von Heizungsanlagen, Lüftungsanlagen und Sanitäranlagen
Zielgruppe
Installation, Wartung und Modernisierung von Heizungsanlagen, Lüftungsanlagen und Sanitäranlagen
Zielgruppe: Firmen und Unternehmen aus der Immobilienwirtschaft, der Industrie sowie Privathaushalte
Aufgabenstellung
- in Adobe Photoshop
- nur die Startseite layouten
- Farben an das Logo angelehnt
- es soll einen blauen Streifen im Projekt geben. siehe pdf Logo

```html
<!DOCTYPE html>
<html lang="de">
<head>
<meta charset="utf-8">
<title>Haustechnik Lindfeld GmbH – Startseite</title>
<link href="https://fonts.googleapis.com/css2?family=Barlow:wght@300;400;500;600;700&family=Tinos&display=swap" rel="stylesheet">
<style>
:root{
  --navy:#0f1650;
  --nav:#27337a;
  --nav-active:#6f79b3;
  --tile:#434a7a;
  --promo:#3d4db0;
  --btn:#dcdff0;
  --ink:#1c2466;
  --white:#fff;
}
*{margin:0;padding:0;box-sizing:border-box}
html,body{width:675px;height:1200px;overflow:hidden}
body{font-family:"Barlow",Arial,sans-serif;background:#fff;position:relative;color:var(--ink)}
.abs{position:absolute}
.site-header{left:0;top:0;width:675px;height:76px;display:flex;flex-direction:column;align-items:center;justify-content:center}
.brand-name{font-weight:400;font-size:26px;color:var(--nav);letter-spacing:.5px;line-height:1}
.brand-sub{font-weight:300;font-size:12px;color:#222;margin-top:6px;letter-spacing:.3px}
.main-nav{left:0;top:76px;width:675px;height:26.5px;background:var(--nav)}
.main-nav a{position:absolute;top:0;height:26.5px;line-height:26.5px;color:var(--white);font-size:14.5px;text-decoration:none}
.main-nav .current{font-weight:700;text-decoration:underline}
.main-nav .open{background:var(--nav-active);padding:0 4px}
.dropdown{left:231px;top:102px;width:116px;height:192px;background:#fff;z-index:3}
.dropdown div{height:32px;border-bottom:1px solid #9aa;display:flex;align-items:center;justify-content:center;font-weight:600;font-size:13.5px;color:#111}
.dropdown div:last-child{border:none}
.hero{left:0;top:102px;width:675px;height:245px;background:linear-gradient(120deg,#d9dade 0%,#8c8f99 30%,#c7c9d0 50%,#7b7f8c 75%,#a5a8b3 100%)}
.catalog{left:0;top:312px;width:145px;height:64px;background:rgba(20,20,20,.85);padding:6px 9px;font-family:"Tinos",serif;font-size:14px;line-height:17px;color:#fff;z-index:2}
.catalog span{text-decoration:underline}
.hero-box{left:352px;top:246px;width:247px;height:92px;background:rgba(61,77,176,.95);padding:17px 12px}
.hero-box h2{color:#fff;font-weight:500;font-size:17.5px}
.btn{display:inline-block;background:var(--btn);color:var(--ink);text-decoration:underline;border:2px solid #9ea3c9;font-size:12.5px;padding:4px 6px}
.hero-box .btn{margin-top:13px}
.content{left:0;top:347px;width:675px;height:611px;background:linear-gradient(180deg,#8a90b5 0%,#d7d9e8 25%,#fff 50%,#e3e5ee 68%,#a3a8c6 90%)}
.welcome{left:0;top:370px;width:675px;text-align:center;color:#fff;font-weight:700;font-size:17.5px;letter-spacing:-.3px}
.intro{font-size:7px;line-height:11px;text-decoration:underline;color:var(--ink);text-align:justify}
.intro p+p{margin-top:11px}
.tile{top:605px;width:86px;height:111px;background:var(--tile);color:#fff;text-align:center}
.tile svg{margin-top:12px}
.tile span{display:block;text-decoration:underline;font-size:14px;margin-top:6px}
.feature{left:66px;top:754px;width:563px;height:163px;background:var(--navy)}
.feature .text{position:absolute;left:304px;top:27px;width:250px;color:#fff}
.feature h3{font-family:"Tinos",serif;font-weight:400;font-size:17.5px}
.feature p{font-size:14px;line-height:20px;margin-top:2px}
.feature .btn{position:absolute;left:298px;top:122px;border:none;font-size:14px;padding:3px 7px;background:#d8d9e0}
.jobs-photo{left:0;top:958px;width:324px;height:190px;background:linear-gradient(100deg,#c9c4bd 0%,#8d8a87 40%,#d6cfc4 70%,#a9a59f 100%)}
.jobs-bg{left:324px;top:958px;width:351px;height:190px;background:linear-gradient(135deg,#55586a 0%,#8a8c99 60%,#c0c1c8 100%)}
.jobs-box{left:348px;top:1033px;width:283px;height:103px;background:var(--promo);padding:10px 24px;color:#fff}
.jobs-box h2{font-weight:500;font-size:17.5px;line-height:26px}
.jobs-box .btn{margin-top:3px;font-size:12.5px}
.site-footer{left:0;top:1148px;width:675px;height:52px;background:var(--navy);color:#fff;text-align:center}
.site-footer .addr{font-size:8.6px;font-weight:500;text-decoration:underline;margin-top:17px}
.site-footer .legal{font-size:5.6px;font-weight:600;text-decoration:underline;margin-top:6px}
</style>
</head>
<body>
<header class="site-header abs">
  <div class="brand-name">Haustechnik Lindfeld</div>
  <div class="brand-sub">Haustechnik Lindfeld GmbH</div>
</header>

<nav class="main-nav abs">
  <a class="current" style="left:186px">Home</a>
  <a class="open" style="left:231px">Dienstleistungen</a>
  <a style="left:356px">Norvia</a>
  <a style="left:406px">Jobs</a>
  <a style="left:444px">Kontakt</a>
</nav>

<div class="hero abs" role="img" aria-label="Foto von verchromten Rohrfittings und Werkzeug auf einem Bauplan"></div>

<div class="dropdown abs">
  <div>Wer sind wir</div><div>Heizungen</div><div>Lüften</div><div>Sanitär</div><div>Rohre</div><div>Dach</div>
</div>

<div class="catalog abs"><span>Bestellen Sie<br>jetzt Ihren<br>Norvia Katalog!</span></div>

<div class="hero-box abs">
  <h2>Haustechnik vom Profi!</h2>
  <a class="btn">Kontaktieren Sie uns!</a>
</div>

<section class="content abs"></section>
<h1 class="welcome abs">Herzlich Willkommen bei Haustechnik Lindfeld</h1>

<div class="intro abs" style="left:69px;top:433px;width:235px">
  <p>Seit 1997 installieren, warten und modernisieren wir Heizungsanlagen, Lüftungsanlagen und Sanitäranlagen nach aktuellsten Standards. Zu unseren Leistungen gehören zudem alle anfallenden Dachklempnerarbeiten, sowohl in der Sanierung, als auch im Neubau, und werden durch professionelle Rohrleitungsbauarbeiten komplettiert.</p>
  <p>Schon zahlreiche Firmen und Unternehmen aus der Immobilienwirtschaft, der Industrie sowie Privathaushalte profitieren von unseren handwerkübergreifenden Dienstleistungen aus einer Hand.</p>
</div>
<div class="intro abs" style="left:367px;top:432px;width:246px">
  <p>Unsere 7 qualifizierten Mitarbeiter werden ständig geschult um Ihnen modernste Haustechnik-Systeme anbieten zu können. Dadurch nutzen Sie den Vorteil, Kosten zu sparen, die Umwelt zu schonen und unter gegebenen Voraussetzungen förderfähig zu modernisieren.</p>
  <p style="margin-top:25px">Haustechnik Lindfeld GmbH – Seit über 15 Jahren im Dienste unserer Kunden.</p>
</div>

<div class="tile abs" style="left:69px">
  <svg width="66" height="48" viewBox="0 0 66 48" fill="none" stroke="#fff" stroke-width="3"><path d="M2 10h12M2 16h10M46 8h8M46 36h8"/><circle cx="7" cy="34" r="4"/><path d="M7 38v8M14 34h4"/><rect x="18" y="4" width="6" height="42" rx="3"/><rect x="25" y="4" width="6" height="42" rx="3"/><rect x="32" y="4" width="6" height="42" rx="3"/><rect x="39" y="4" width="6" height="42" rx="3"/></svg>
  <span style="font-size:16px;margin-top:2px">Heizung</span>
</div>
<div class="tile abs" style="left:227px">
  <svg width="54" height="54" viewBox="0 0 54 54" fill="none" stroke="#fff" stroke-width="2.5"><rect x="2" y="2" width="50" height="50" rx="3"/><circle cx="27" cy="27" r="20"/><circle cx="27" cy="27" r="4"/><path d="M27 23c0-8 6-12 12-8M31 27c8 0 12 6 8 12M27 31c0 8-6 12-12 8M23 27c-8 0-12-6-8-12"/><circle cx="7" cy="7" r="1.5"/><circle cx="47" cy="7" r="1.5"/><circle cx="7" cy="47" r="1.5"/><circle cx="47" cy="47" r="1.5"/></svg>
  <span>Lüften</span>
</div>
<div class="tile abs" style="left:386px">
  <svg width="54" height="54" viewBox="0 0 54 54" fill="none" stroke="#fff" stroke-width="2.5"><path d="M2 28h50M4 28c0 10 10 16 23 16s23-6 23-16M22 44v8M32 44v8M24 22V8a4 4 0 0 1 8 0v6M16 22v-4M38 22v-4M12 22h30"/></svg>
  <span>Sanitär</span>
</div>
<div class="tile abs" style="left:543px">
  <svg width="58" height="54" viewBox="0 0 58 54" fill="none" stroke="#fff" stroke-width="2.5"><path d="M2 6h12v10h8v14a10 10 0 0 0 20 0V22h10V10h4"/><path d="M14 4v14M52 8v16M28 22v8a4 4 0 0 0 8 0v-8"/></svg>
  <span>Rohre</span>
</div>

<section class="feature abs">
  <svg class="abs" style="left:14px;top:24px" width="162" height="113" viewBox="0 0 66 46" fill="none" stroke="#fff" stroke-width="2.6"><path d="M2 10h12M2 16h10M46 8h8M46 38h8M46 24h6"/><circle cx="7" cy="34" r="4"/><path d="M7 38v8M11 34h7"/><rect x="18" y="2" width="6" height="42" rx="3"/><rect x="25" y="2" width="6" height="42" rx="3"/><rect x="32" y="2" width="6" height="42" rx="3"/><rect x="39" y="2" width="6" height="42" rx="3"/></svg>
  <div class="text">
    <h3>Lorem Ipsum</h3>
    <p>sed diam nonumy eirmod tempor invidunt ut labore et dolore magna aliquyam erat</p>
  </div>
  <a class="btn">Heinzungskonfigurator</a>
</section>

<div class="jobs-bg abs"></div>
<div class="jobs-photo abs" role="img" aria-label="Foto eines lächelnden Handwerkers in Latzhose mit gelbem Schutzhelm"></div>
<div class="jobs-box abs">
  <h2>Du suchst einen Neuanfang?<br>Wir suchen Dich.</h2>
  <a class="btn">Kontaktieren Sie uns!</a>
</div>

<footer class="site-footer abs">
  <p class="addr">Haustechnik Lindfeld GmbH Talweg 12 01234 Musterau Tel.: (01234) 567890 Fax: (01234) 567891 Mobil: (0170) 1234567</p>
  <p class="legal">Impressum und Datenschutz</p>
</footer>
</body>
</html>
```